Flag Design

We want a new updated flag design for our yacht charter company in Greece. We need the logo and colour shceme to be the same but design needs update. Old logo is attached. The flag dimensions must remain the same

Target Market(s)

Sailing

Industry/Entity Type

Marine

Colors
0054AA
0677BA
7BADD7
CADEEF
E8F1F8

```html
<!DOCTYPE html>
<html lang="en">
<head>
<meta charset="UTF-8">
<title>Vela Maris – Flag Banner</title>
<link href="https://fonts.googleapis.com/css2?family=Montserrat:wght@700&display=swap" rel="stylesheet">
<style>
  :root {
    --backdrop: #d6d6d6;
    --navy: #1d2038;
    --wave-deep: #263a78;
    --wave-royal: #0054AA;
    --wave-ocean: #0677BA;
    --wave-sky: #7BADD7;
    --wave-mist: #CADEEF;
    --brand-cyan: #3fbfea;
  }
  html, body {
    margin: 0;
    padding: 0;
    width: 848px;
    height: 1200px;
    overflow: hidden;
    background: var(--backdrop);
  }
  .flag {
    position: absolute;
    left: 134px;
    top: 60px;
    width: 580px;
    height: 1080px;
    background: var(--navy);
    overflow: hidden;
  }
  .flag__sea {
    position: absolute;
    inset: 0;
    width: 100%;
    height: 100%;
  }
  .flag__brand {
    position: absolute;
    top: 56px;
    right: 96px;
    display: flex;
    align-items: flex-end;
    gap: 14px;
  }
  .flag__brand-name {
    writing-mode: vertical-rl;
    transform: rotate(180deg);
    text-align: start;
    font-family: "Montserrat", sans-serif;
    font-weight: 700;
    font-size: 112px;
    line-height: 0.98;
    letter-spacing: 2px;
    color: var(--brand-cyan);
    margin: 0;
    height: 520px;
  }
  .flag__brand-dot {
    width: 56px;
    height: 56px;
    border-radius: 50%;
    background: var(--brand-cyan);
    margin-bottom: 4px;
  }
</style>
</head>
<body>
  <div class="flag">
    <svg class="flag__sea" viewBox="0 0 580 1080" preserveAspectRatio="none" role="img" aria-label="Layered ocean wave artwork sweeping up from the lower left to the right edge">
      <defs>
        <linearGradient id="sea-tone" x1="0" y1="0" x2="1" y2="1">
          <stop offset="0" stop-color="var(--wave-deep)"/>
          <stop offset="0.45" stop-color="var(--wave-royal)"/>
          <stop offset="0.75" stop-color="var(--wave-ocean)"/>
          <stop offset="1" stop-color="var(--wave-sky)"/>
        </linearGradient>
      </defs>
      <path fill="url(#sea-tone)" d="M580 640 C545 780 400 810 260 850 C150 880 50 940 0 1010 L0 1080 L580 1080 Z"/>
    </svg>
    <div class="flag__brand">
      <div class="flag__brand-dot"></div>
      <h1 class="flag__brand-name">VELA<br>MARIS</h1>
    </div>
  </div>
</body>
</html>
```